Progressive Flow Chart

Looking for a progressive flow chart centered and branching off. They all build on each other 1-3. There will be 3 different pages.

Target Market(s)

Business Owners - High Net worth Individuals

Industry/Entity Type

Finance & Business Consulting

Font styles to use
Serif

Colors
0054AA
0677BA
7BADD7
CADEEF
E8F1F8
0094D4
00A9DD
6FCCEA
C7EBF8
E9F6FB
00AB8E
00BBA5
67D7C9
C6EFE9
E9F9F6

Requirements
Nice to have
• Clean, simple, and approachable.
Should not have
• Very Busy

```html
<!DOCTYPE html>
<html lang="en">
<head>
<meta charset="utf-8">
<title>Living Trust Flow Chart – Three Pages</title>
<link href="https://fonts.googleapis.com/css2?family=Lato:wght@400;700;900&display=swap" rel="stylesheet">
<style>
  :root {
    --board: #333333;
    --page: #ffffff;
    --navy: #141a45;
    --teal: #1de3b8;
    --teal-deep: #10c9a5;
    --sky: #29aedd;
    --sky-light: #8ec9ee;
    --ring-soft: #cfe8f4;
    --label: #111111;
    --muted: #8a8a8a;
    --white: #ffffff;
  }
  html, body {
    margin: 0;
    padding: 0;
    width: 834px;
    height: 1200px;
    overflow: hidden;
    background: var(--board);
  }
  .board { display: block; width: 834px; height: 1200px; }
  .sheet { fill: var(--page); }
  .entity-frame { fill: var(--white); stroke: var(--navy); stroke-width: 2.5; }
  .entity-dot { fill: var(--navy); }
  .entity-name { font-family: 'Lato', sans-serif; font-weight: 700; font-size: 15px; fill: var(--muted); }
  .brand-disc { fill: var(--navy); }
  .brand-name { font-family: 'Lato', sans-serif; font-weight: 700; font-size: 22px; letter-spacing: 3px; fill: var(--white); }
  .ring-white { fill: var(--white); }
  .ring-outline { fill: var(--white); stroke: var(--ring-soft); stroke-width: 3; }
  .arc-title { font-family: 'Lato', sans-serif; font-weight: 900; font-size: 25px; letter-spacing: 6px; fill: var(--white); }
  .arc-sub { font-family: 'Lato', sans-serif; font-weight: 900; font-size: 16px; letter-spacing: 1.5px; fill: var(--teal-deep); }
  .box-light { fill: var(--sky-light); }
  .box-grad { fill: url(#boxGradient); }
  .box-text { font-family: 'Lato', sans-serif; font-weight: 700; fill: var(--white); text-anchor: middle; }
  .box-text.small { font-size: 12px; }
  .box-text.large { font-size: 14.5px; }
  .icon-disc { fill: var(--white); }
  .icon-line { fill: none; stroke: #1f2a44; stroke-width: 1.6; stroke-linejoin: round; stroke-linecap: round; }
  .icon-line-white { fill: none; stroke: var(--white); stroke-width: 2; stroke-linejoin: round; stroke-linecap: round; }
  .flow-teal { stroke: var(--teal); fill: none; stroke-width: 10; }
  .flow-sky { stroke: var(--sky); fill: none; stroke-width: 10; }
  .connector { stroke: var(--teal); fill: none; stroke-width: 6; }
  .head-teal { fill: var(--teal); }
  .head-sky { fill: var(--sky); }
  .flow-label { font-family: 'Lato', sans-serif; font-weight: 900; font-size: 11px; fill: var(--label); }
  .credit { font-family: 'Lato', sans-serif; font-size: 8px; fill: #333; text-anchor: end; }
</style>
</head>
<body>
<svg class="board" viewBox="0 0 1000 1439" xmlns="http://www.w3.org/2000/svg">
  <defs>
    <linearGradient id="ringGradient" x1="0" y1="0" x2="0" y2="1">
      <stop offset="0" stop-color="#1de6b6"/>
      <stop offset="1" stop-color="#2ab0e2"/>
    </linearGradient>
    <linearGradient id="boxGradient" x1="0" y1="0" x2="1" y2="0">
      <stop offset="0" stop-color="#2ab2e0"/>
      <stop offset="1" stop-color="#1de6b6"/>
    </linearGradient>
    <path id="arcOuter" d="M406,382 A103,103 0 0 1 612,382"/>
    <path id="arcInner" d="M430,382 A79,79 0 0 1 588,382"/>

    <!-- entity tiles across the top -->
    <g id="entity-row">
      <rect class="entity-frame" x="154" y="123" width="169" height="71" rx="10"/>
      <circle class="entity-dot" cx="191" cy="158" r="27"/>
      <text class="entity-name" x="229" y="164">CRT</text>

      <rect class="entity-frame" x="424" y="123" width="169" height="71" rx="10"/>
      <circle class="entity-dot" cx="459" cy="158" r="27"/>
      <text class="entity-name" x="500" y="164">DAF</text>

      <rect class="entity-frame" x="699" y="123" width="169" height="71" rx="10"/>
      <circle class="entity-dot" cx="734" cy="158" r="27"/>
      <text class="entity-name" x="773" y="156">GRAT’S</text>
      <text class="entity-name" x="773" y="172">IDGT’S</text>
    </g>

    <!-- trust hub core -->
    <g id="hub-core">
      <circle class="brand-disc" cx="509" cy="382" r="72"/>
      <text class="brand-name" x="509" y="390" text-anchor="middle">ORVALE</text>
      <text class="arc-sub"><textPath href="#arcInner" startOffset="56%" text-anchor="middle">YOU TRUSTEE</textPath></text>
    </g>

    <!-- full trust hub with gradient ring -->
    <g id="hub-full">
      <circle cx="509" cy="382" r="125" fill="url(#ringGradient)"/>
      <circle class="ring-white" cx="509" cy="382" r="96"/>
      <text class="arc-title"><textPath href="#arcOuter" startOffset="51%" text-anchor="middle">LIVING TRUST</textPath></text>
      <use href="#hub-core"/>
    </g>

    <!-- hub shown with a light outline only -->
    <g id="hub-outline">
      <circle class="ring-outline" cx="509" cy="382" r="98"/>
      <use href="#hub-core"/>
    </g>

    <!-- bank investment branch -->
    <g id="bank-branch">
      <rect class="box-light" x="150" y="352" width="170" height="73" rx="8"/>
      <circle class="icon-disc" cx="186" cy="388" r="26" opacity="0.25"/>
      <g class="icon-line-white">
        <path d="M170,381 L186,370 L202,381 Z"/>
        <path d="M174,384 V400 M181,384 V400 M191,384 V400 M198,384 V400"/>
        <path d="M169,403 H203"/>
      </g>
      <text class="box-text small" x="266" y="371">BANK MAKES</text>
      <text class="box-text small" x="266" y="384">INVESTMENT</text>
      <text class="box-text small" x="266" y="398">IN REAL ESTATE</text>
      <text class="box-text small" x="266" y="411">+ BUSINESS</text>
      <line class="flow-teal" x1="382" y1="390" x2="343" y2="390"/>
      <polygon class="head-teal" points="346,377 325,390 346,403"/>
      <text class="flow-label" x="334" y="373">INVEST</text>
    </g>

    <!-- insurance branch -->
    <g id="insurance-branch">
      <path class="connector" d="M632,382 H780 Q795,382 795,397 V572"/>
      <rect class="box-light" x="699" y="572" width="169" height="71" rx="8"/>
      <circle cx="734" cy="607" r="27" fill="none" stroke="#ffffff" stroke-width="1.5" opacity="0.8"/>
      <g class="icon-line-white">
        <path d="M734,592 L746,597 V607 Q746,617 734,622 Q722,617 722,607 V597 Z"/>
        <path d="M728,607 L733,612 L741,602"/>
      </g>
      <text class="box-text large" x="813" y="614">INSURANCE</text>
    </g>

    <!-- interest and investment loop -->
    <g id="lending-loop">
      <line class="flow-teal" x1="182" y1="560" x2="182" y2="458" style="stroke-width:9"/>
      <polygon class="head-teal" points="170,460 182,438 194,460"/>
      <line class="flow-teal" x1="222" y1="440" x2="222" y2="542" style="stroke-width:9"/>
      <polygon class="head-teal" points="210,540 222,562 234,540"/>
      <text class="flow-label" transform="translate(176,527) rotate(-90)">INTEREST</text>
      <text class="flow-label" transform="translate(216,533) rotate(-90)">INVESTMENT</text>
    </g>

    <!-- real estate and business branch -->
    <g id="operating-branch">
      <path class="flow-sky" d="M295,570 V447 Q295,435 307,435 H364"/>
      <polygon class="head-sky" points="362,422 384,435 362,448"/>
      <text class="flow-label" transform="translate(285,531) rotate(-90)">INCOME</text>

      <rect class="box-grad" x="150" y="570" width="170" height="72" rx="8"/>
      <circle class="icon-disc" cx="187" cy="606" r="27"/>
      <g class="icon-line">
        <path d="M176,606 L187,596 L198,606"/>
        <path d="M179,604 V616 H195 V604"/>
        <path d="M185,616 V609 H190 V616"/>
      </g>
      <text class="box-text large" x="265" y="607">REAL ESTATE</text>
      <text class="box-text large" x="265" y="623">LLC</text>

      <line class="flow-sky" x1="330" y1="606" x2="400" y2="606" style="stroke-width:8"/>
      <polygon class="head-sky" points="398,594 419,606 398,618"/>
      <text class="flow-label" x="355" y="600">RENT</text>

      <rect class="box-grad" x="424" y="570" width="169" height="72" rx="8"/>
      <circle class="icon-disc" cx="460" cy="606" r="27"/>
      <g class="icon-line">
        <circle cx="460" cy="600" r="7"/>
        <path d="M446,617 L453,611 H467 L474,617"/>
        <path d="M454,611 L460,617 L466,611"/>
      </g>
      <text class="box-text small" x="539" y="596">BUSINESS LLC</text>
      <text class="box-text small" x="539" y="611">MEMBER/MGR</text>
      <text class="box-text small" x="539" y="627">BRP=PRESIDENT</text>

      <line class="flow-sky" x1="509" y1="562" x2="509" y2="530"/>
      <polygon class="head-sky" points="496,532 509,510 522,532"/>
      <text class="flow-label" x="518" y="551">TRY ON</text>
    </g>

    <text id="icon-credit" class="credit" x="865" y="667">Icons by Pixelmint and Hollowleaf from Iconvault.com</text>
  </defs>

  <rect width="1000" height="1439" fill="var(--board)"/>

  <!-- page: complete overview -->
  <g class="page page-overview">
    <rect class="sheet" x="126" y="87" width="767" height="594"/>
    <use href="#entity-row"/>
    <use href="#hub-full"/>
    <use href="#bank-branch"/>
    <use href="#lending-loop"/>
    <use href="#operating-branch"/>
    <use href="#insurance-branch"/>
    <use href="#icon-credit"/>
  </g>

  <!-- page 1: operating structure -->
  <g class="page page-step-one">
    <rect class="sheet" x="126" y="758" width="374" height="288"/>
    <g transform="translate(126,758) scale(0.4876) translate(-126,-87)">
      <use href="#hub-full"/>
      <use href="#operating-branch"/>
      <use href="#icon-credit"/>
    </g>
  </g>

  <!-- page 2: investment and protection -->
  <g class="page page-step-two">
    <rect class="sheet" x="519" y="758" width="374" height="288"/>
    <g transform="translate(519,758) scale(0.4876) translate(-126,-87)">
      <use href="#hub-outline"/>
      <use href="#bank-branch"/>
      <use href="#insurance-branch"/>
      <use href="#icon-credit"/>
    </g>
  </g>

  <!-- page 3: planning vehicles -->
  <g class="page page-step-three">
    <rect class="sheet" x="321" y="1067" width="377" height="291"/>
    <g transform="translate(321,1067) scale(0.4915) translate(-126,-87)">
      <use href="#entity-row"/>
      <use href="#hub-outline"/>
    </g>
  </g>
</svg>
</body>
</html>
```